Elegant Black Candle Label Design!

I need a 2.375" tall by 3.0" wide candle label design. I'm looking for simple and elegant. Black label with silver leaf border and lettering. Label needs to have the following information on it: Fern Hollow Candle Co. as the company name, scent name in the middle and in smaller font, it needs to say Made in USA, All Natural, 8oz. Attached photos are for inspiration.

Target Market(s)

People looking for high end, all natural candle fragrances

Industry/Entity Type

Candle-Spa

Colors

Designer to choose only greyscale colors for use in the design.

Requirements
Must have
• Company Name, Scent (ability to change scent names), All Natural, Made in USA, 8oz
Nice to have
• Black background, silver leaf border and silver leaf font. Elegant fonts maybe slightly cursive

```html
<!DOCTYPE html>
<html lang="en">
<head>
<meta charset="UTF-8">
<title>Fern Hollow Candle Co. — Sandlewood Label</title>
<link href="https://fonts.googleapis.com/css2?family=Sacramento&family=Poppins:wght@300;400&display=swap" rel="stylesheet">
<style>
  :root {
    --page-bg: #f2f0e8;
    --label-black: #0d0d0d;
    --silver: #e6e6e6;
    --silver-soft: #bdbdbd;
    --leaf-tone: #3a3a3a;
  }
  * { box-sizing: border-box; margin: 0; padding: 0; }
  html, body {
    width: 1200px;
    height: 900px;
    overflow: hidden;
    background: var(--page-bg);
  }
  .canvas {
    width: 1200px;
    height: 900px;
    display: flex;
    align-items: center;
    justify-content: center;
  }
  .label {
    position: relative;
    width: 840px;
    height: 665px;
    background: var(--label-black);
    color: var(--silver);
  }
  .label-frame {
    position: absolute;
    inset: 30px;
    border: 2px solid var(--silver);
  }
  .sprig {
    position: absolute;
    width: 52px;
    height: 230px;
    background: linear-gradient(180deg, var(--leaf-tone), #5a5a5a, var(--leaf-tone));
    border-radius: 26px;
  }
  .sprig--top-right { top: 46px; right: 46px; }
  .sprig--bottom-left { bottom: 46px; left: 46px; }
  .company-name {
    position: absolute;
    top: 140px;
    left: 120px;
    right: 120px;
    text-align: center;
    font-family: "Sacramento", cursive;
    font-size: 56px;
    font-weight: 400;
    line-height: 1.2;
    white-space: nowrap;
  }
  .scent-name {
    position: absolute;
    top: 282px;
    left: 0;
    right: 0;
    display: flex;
    align-items: center;
    justify-content: center;
    gap: 32px;
    font-family: "Poppins", sans-serif;
    font-weight: 300;
    font-size: 40px;
    letter-spacing: 1px;
  }
  .sparkle { width: 20px; height: 20px; fill: var(--silver); }
  .sparkle--low { transform: translateY(20px); }
  .sparkle--high { transform: translateY(-20px); }
  .details {
    position: absolute;
    top: 468px;
    left: 0;
    right: 0;
    display: flex;
    flex-direction: column;
    align-items: center;
    font-family: "Poppins", sans-serif;
    font-weight: 300;
    font-size: 28px;
    letter-spacing: 0.5px;
  }
  .details-rule {
    width: 380px;
    height: 2px;
    background: var(--silver);
    margin: 10px 0 14px;
  }
</style>
</head>
<body>
  <main class="canvas">
    <section class="label">
      <div class="label-frame"></div>
      <div class="sprig sprig--top-right" role="img" aria-label="Silver leaf sprig ornament"></div>
      <div class="sprig sprig--bottom-left" role="img" aria-label="Silver leaf sprig ornament"></div>

      <h1 class="company-name">Fern Hollow Candle Co.</h1>

      <p class="scent-name">
        <svg class="sparkle sparkle--low" viewBox="0 0 20 20" aria-hidden="true"><path d="M10 0 L12 8 L20 10 L12 12 L10 20 L8 12 L0 10 L8 8 Z"/></svg>
        <span>Sandlewood</span>
        <svg class="sparkle sparkle--high" viewBox="0 0 20 20" aria-hidden="true"><path d="M10 0 L12 8 L20 10 L12 12 L10 20 L8 12 L0 10 L8 8 Z"/></svg>
      </p>

      <div class="details">
        <span class="details-line">All Nutural • 8 oz.</span>
        <span class="details-rule"></span>
        <span class="details-line">Made in USA</span>
      </div>
    </section>
  </main>
</body>
</html>
```